Learning Habits- Teaching and Learning Policy

Hi,

The philosophy behind this Teaching and Learning Policy is to equip young people (Age 16-18) for many challenges that lies ahead. The pace of technological advancement is so great that it is probable that many jobs our students will do in their lifetime do not yet even exist. We realise that we need to help develop our students into effective lifelong learners – meaning that they will:

-Need to be independent whilst also being able to work as a team.
-Need to apply many different strategies to help take on new concepts.
-Reflect on current practice, and improve.

I have attached the file which has the basic designs of the 4 different leaner habits and what they entail. Each habit is colour coordinated, so please keep the colours the same.

Collaboration- Blue (royal blue)
Persevering- Red
Planning- Orange
Reflection- Yellow

I would ideally like the poster to be transferable into a powerpoint too.

Thanking you all so much.

Perla
Updates

Project Deadline Extended Reason: Hi,I am extending this deadline as I will be requesting some changes to the title / slogan.I need the four learning habits have a catchy name which will motivate students.Please send me some suggestions.Thanking you all.Perla Added Monday, March 28, 2016

Target Market(s)

Teachers and students (age 16-18)

Industry/Entity Type

Education

Font styles to use
Other font styles liked:
• Something friendly to kids- where the a is printed like it is written. Similar to century gothic but more friendly.

Requirements
Must have
• Laid out similar to the the website attached. Interesting, motivational yet educational to students in how they can become lifelong learners.
Nice to have
• I should be able to transfer this to a powerpoint from a poster.
• It can be four posters or one depending on the design.
Should not have
• Each Habit must be colour-coordinated:
• Collaboration- Blue (royal blue)
• Persevering- Red
• Planning- Orange
• Reflection- Yellow
• Thank you,

```html
<!DOCTYPE html>
<html lang="en">
<head>
<meta charset="utf-8">
<title>Learning Habits</title>
<link href="https://fonts.googleapis.com/css2?family=Ubuntu:wght@700&display=swap" rel="stylesheet">
<style>
  :root {
    --royal-blue: #2b3b9c;
    --red: #c21f33;
    --orange: #ec9726;
    --yellow: #ecd912;
    --paper: #fcfcfd;
    --ink-light: #ffffff;
    --ink-dark: #3b3416;
  }
  html, body {
    margin: 0;
    padding: 0;
    overflow: hidden;
    background: var(--paper);
  }
  .poster {
    position: relative;
    width: 873px;
    height: 1200px;
    overflow: hidden;
    background: var(--paper);
    font-family: "Ubuntu", "Trebuchet MS", sans-serif;
  }
  .waves {
    position: absolute;
    inset: 0;
    width: 873px;
    height: 1200px;
  }
  .habit {
    position: absolute;
    width: 334px;
    height: 334px;
    border-radius: 50%;
    display: flex;
    flex-direction: column;
    align-items: center;
    justify-content: center;
    color: var(--ink-light);
  }
  .habit-name {
    margin: 22px 0 0;
    font-size: 44px;
    font-weight: 700;
    letter-spacing: -0.5px;
    line-height: 1;
  }
  .habit-icon {
    margin-top: 20px;
    width: 90px;
    height: 72px;
  }
  .habit-icon.pictogram {
    background: rgba(255, 255, 255, 0.85);
    border-radius: 8px;
  }
  .habit--collaboration { left: 87px; top: 255px; background: var(--royal-blue); }
  .habit--persevering { left: 447px; top: 255px; background: var(--red); }
  .habit--planning { left: 87px; top: 609px; background: var(--orange); }
  .habit--reflection { left: 447px; top: 609px; background: var(--yellow); color: var(--ink-dark); }
</style>
</head>
<body>
<main class="poster">
  <svg class="waves" viewBox="0 0 873 1200" preserveAspectRatio="none" aria-hidden="true">
    <path class="wave-top-accent" fill="var(--orange)"
          d="M0 0 H873 V200 C760 200 640 170 520 130 C380 85 200 64 0 62 Z"/>
    <path class="wave-top-band" fill="var(--royal-blue)"
          d="M0 0 H873 V158 C760 158 640 140 520 112 C380 78 200 54 0 52 Z"/>
    <path class="wave-bottom-accent" fill="var(--yellow)"
          d="M0 1004 C160 980 300 985 430 1025 C570 1068 720 1100 873 1100 V1200 H0 Z"/>
    <path class="wave-bottom-band" fill="var(--red)"
          d="M0 1032 C160 1010 300 1015 430 1055 C570 1098 720 1150 873 1158 V1200 H0 Z"/>
  </svg>

  <section class="habit habit--collaboration">
    <h2 class="habit-name">Collaboration</h2>
    <div class="habit-icon pictogram" role="img" aria-label="Pictogram of three people standing together"></div>
  </section>

  <section class="habit habit--persevering">
    <h2 class="habit-name">Persevering</h2>
    <div class="habit-icon pictogram" role="img" aria-label="Pictogram of a climber scaling a rock wall"></div>
  </section>

  <section class="habit habit--planning">
    <h2 class="habit-name">Planning</h2>
    <div class="habit-icon pictogram" role="img" aria-label="Pictogram of a person drawing a plan on a board"></div>
  </section>

  <section class="habit habit--reflection">
    <h2 class="habit-name">Reflection</h2>
    <svg class="habit-icon" viewBox="0 0 90 72" role="img" aria-label="Speech bubbles icon">
      <path d="M8 10 h40 a8 8 0 0 1 8 8 v16 a8 8 0 0 1 -8 8 h-22 l-12 10 v-10 h-6 a8 8 0 0 1 -8 -8 v-16 a8 8 0 0 1 8 -8 z"
            fill="none" stroke="var(--ink-dark)" stroke-width="5" stroke-linejoin="round"/>
      <path d="M62 24 h12 a8 8 0 0 1 8 8 v14 a8 8 0 0 1 -8 8 h-2 v10 l-12 -10 h-18 a8 8 0 0 1 -8 -8 v-2"
            fill="none" stroke="var(--ink-dark)" stroke-width="5" stroke-linejoin="round"/>
    </svg>
  </section>
</main>
</body>
</html>
```